Meridane Works, Inc. - Update our Website

Meridane Works needs a website to help our customers to navigate through our services efficiently. Our existing website is at www.meridwork.example

We would like to explain our services with content and pictures (photographs) that distinguishes our products and services from our competition.

The website design must implement a strategy to focus on our Contract Labeling services.

With this new design we would like to attract new customers and ensure that our existing customers are fully informed with our latest offerings.

```html
<!DOCTYPE html>
<html lang="en">
<head>
<meta charset="utf-8">
<title>Meridane Works, Inc.</title>
<link href="https://fonts.googleapis.com/css2?family=Open+Sans:wght@400;600;700&family=Lora:wght@400&display=swap" rel="stylesheet">
<style>
:root{
  --topbar:#4a4a4a;
  --ink:#222;
  --text:#555;
  --muted:#777;
  --blue:#1a7fb0;
  --green:#8cc63f;
  --red:#e0412a;
  --band:#ececec;
  --rule:#dcdcdc;
  --footer-head:#7aa52a;
}
*{margin:0;padding:0;box-sizing:border-box}
html,body{width:1200px;height:2240px;overflow:hidden;background:#fff}
body{position:relative;font-family:"Open Sans",Arial,sans-serif;color:var(--text)}
.abs{position:absolute}
.topbar{left:0;top:0;width:1200px;height:34px;background:linear-gradient(#5a5a5a,#3c3c3c)}
.topbar .contact{right:330px;top:9px;color:#eee;font-size:12px;display:flex;gap:30px}
.topbar .contact span{display:flex;align-items:center;gap:8px}
.topbar .social{right:150px;top:9px;display:flex;gap:6px}
.dot{width:16px;height:16px;border-radius:50%;background:#888;display:block}
.header{left:0;top:34px;width:1200px;height:85px;background:#fff}
.brand{display:flex;align-items:center;gap:10px;font-weight:700;color:var(--ink);letter-spacing:.5px}
.brand .mark{border-radius:50%;background:var(--green)}
.header .brand{left:150px;top:30px;font-size:17px}
.header .brand .mark{width:26px;height:26px}
.nav{right:150px;top:36px;display:flex;gap:20px;font-size:13.5px;color:#333}
.hero{left:0;top:119px;width:1200px;height:370px;background:linear-gradient(100deg,#f5a133 0%,#ea7a22 35%,#c8632c 55%,#3d7f8c 80%,#276f7f 100%)}
.hero h1{left:210px;top:90px;font-family:"Lora",Georgia,serif;font-weight:400;font-size:36px;color:#2b2b2b}
.hero h2{left:210px;top:137px;font-family:"Lora",Georgia,serif;font-weight:400;font-size:20px;color:#fff}
.hero p{left:210px;top:172px;width:440px;font-size:14px;color:#fff;line-height:1.35}
.btn{display:flex;align-items:center;justify-content:center;background:var(--green);color:#fff;font-size:14px;gap:8px}
.hero .btn{left:210px;top:226px;width:150px;height:41px}
.hero .visual{left:660px;top:50px;width:400px;height:290px;border-radius:8px;background:linear-gradient(160deg,#e8eef0,#9fb0b6);opacity:.85}
.intro h3{left:0;top:508px;width:1200px;text-align:center;font-weight:400;font-size:26px;color:var(--ink)}
.intro p{left:140px;top:548px;width:920px;text-align:center;font-size:13px;line-height:1.4;color:var(--muted)}
.band{left:0;top:612px;width:1200px;height:69px;background:var(--band)}
.band h3{left:258px;top:14px;font-weight:400;font-size:29px;color:var(--ink)}
.card h4{font-weight:400;font-size:16px;color:var(--blue);position:absolute;left:0;top:0}
.card .pic{position:absolute;left:0;top:22px;width:262px;height:170px}
.card p{position:absolute;left:0;width:262px;font-size:12px;line-height:1.45;color:var(--muted)}
.card .btn{position:absolute;left:0;width:150px;height:42px}
.sep{left:0;width:1200px;height:1px;background:var(--rule)}
.about .brand{left:100px;top:1712px;font-size:30px}
.about .brand .mark{width:48px;height:48px}
.vline{width:1px;background:var(--rule)}
.about h3{left:626px;top:1612px;font-weight:400;font-size:28px;color:var(--ink)}
.about p{left:626px;top:1678px;width:420px;font-size:12px;line-height:1.6;color:var(--text)}
.links{font-size:12px;color:var(--red);line-height:2.3}
.foot h5{font-weight:400;font-size:13px;color:var(--footer-head)}
.foot ul{list-style:none;font-size:11.5px;color:#555;line-height:1.6}
.foot .brand{left:841px;top:1996px;font-size:15px}
.foot .brand .mark{width:24px;height:24px}
.foot address{font-style:normal;font-size:10px;color:#555;line-height:1.5;left:850px;width:260px}
.copy{left:123px;top:2208px;font-size:10px;color:#666}
</style>
</head>
<body>
<div class="abs topbar">
  <div class="abs contact">
    <span><svg width="14" height="10" viewBox="0 0 14 10"><rect x="0.5" y="0.5" width="13" height="9" fill="#ddd"/><path d="M0.5 0.5 7 6 13.5 0.5" fill="none" stroke="#555"/></svg>info@meridwork.example</span>
    <span><svg width="12" height="12" viewBox="0 0 12 12"><path d="M2 1l2 0 1 3-1.5 1a7 7 0 003 3L8 7l3 1v2c0 1-1 1-1 1C5 11 1 7 1 2c0 0 0-1 1-1z" fill="#ddd"/></svg>1-555-010-2040</span>
  </div>
  <div class="abs social"><i class="dot"></i><i class="dot"></i><i class="dot"></i><i class="dot"></i><i class="dot"></i></div>
</div>

<header class="abs header">
  <div class="abs brand"><i class="mark"></i>MERIDANE WORKS</div>
  <nav class="abs nav"><span>Home</span><span>About Us</span><span>Services</span><span>Products</span><span>User Support</span><span>Contact Us</span></nav>
</header>

<section class="abs hero">
  <h1 class="abs">Meridane Works, Inc.</h1>
  <h2 class="abs">Leading Clinical Label Generation System</h2>
  <p class="abs">Meridane Works, Inc. specializes in providing products and services to the pharmaceutical industry.</p>
  <div class="abs btn">Learn More <span>+</span></div>
  <div class="abs visual" role="img" aria-label="Photo of a desktop monitor with a stethoscope and capsules"></div>
</section>

<section class="intro">
  <h3 class="abs">We are focused on the needs of those individuals involved with Clinical Trial Materials.</h3>
  <p class="abs">Lorem ipsum dolor sit amet, consectetur adipiscing elit. In rhoncus nisi et elementum dapibus. Nulla facilisi. Mauris elementum eros justo, id pretium massa mattis quis. Morbi at semper dolor, ac pretium augue.</p>
</section>

<section class="abs band">
  <svg class="abs" style="left:0;top:0" width="240" height="69" viewBox="0 0 240 69"><path d="M0 0H200L232 34.5 200 69H0Z" fill="#f6f6f6"/></svg>
  <h3 class="abs">Our Products &amp; Services</h3>
</section>

<div class="abs card" style="left:170px;top:716px;width:262px;height:360px">
  <h4>MeriServ™</h4>
  <div class="pic" role="img" aria-label="Photo of a clinician holding a tablet" style="background:linear-gradient(135deg,#dfe4e8,#7d8a93)"></div>
  <p style="top:212px">MeriServ™ is a contract clinical label generation service that provides you with ready to apply clinical labels specifically designed and produced for your clinical...</p>
  <div class="btn" style="top:310px">Learn More <span>+</span></div>
</div>
<div class="abs card" style="left:464px;top:716px;width:262px;height:360px">
  <h4>MeriBook™</h4>
  <div class="pic" role="img" aria-label="Photo of stacked compact discs" style="background:linear-gradient(135deg,#5a2ea0,#c03cc6 50%,#3a7fd0)"></div>
  <p style="top:212px">MeriBook™ labels are multi-page clinical labels used to address the needs of multi-language studies. This enables user to prepare and ship clinical materials to multiple...</p>
  <div class="btn" style="top:310px">Learn More <span>+</span></div>
</div>
<div class="abs card" style="left:757px;top:716px;width:262px;height:360px">
  <h4>Clinical Randomizations</h4>
  <div class="pic" role="img" aria-label="Photo of a glowing data microarray slide" style="background:linear-gradient(135deg,#0a1f6a,#1e58c8 55%,#0b2a80)"></div>
  <p style="top:212px">Our systems can create randomization data for all types of CTM requirements. Patient randomization, material randomization and random...</p>
  <div class="btn" style="top:310px">Learn More <span>+</span></div>
</div>

<div class="abs card" style="left:170px;top:1140px;width:262px;height:360px">
  <h4>MeriPro/LBL™</h4>
  <div class="pic" role="img" aria-label="Photo of a gloved hand holding a labelled test tube" style="background:linear-gradient(135deg,#0f3f8a,#2f7fd8 55%,#0c2f70)"></div>
  <p style="top:212px">MeriServ™ is a contract clinical label generation service that provides you with ready to apply clinical labels specifically designed and produced for your clinical...</p>
  <div class="btn" style="top:311px">Learn More <span>+</span></div>
</div>
<div class="abs card" style="left:464px;top:1140px;width:262px;height:360px">
  <h4>Software Validation Services</h4>
  <div class="pic" role="img" aria-label="Photo of a stethoscope resting on a laptop keyboard" style="background:linear-gradient(135deg,#3a3a3e,#1c1c20 60%,#55575c)"></div>
  <p style="top:212px">MeriBook™ labels are multi-page clinical labels used to address the needs of multi-language studies. This enables user to prepare and ship clinical materials to multiple...</p>
  <div class="btn" style="top:311px">Learn More <span>+</span></div>
</div>
<div class="abs card" style="left:757px;top:1140px;width:262px;height:360px">
  <h4>MeriStock™</h4>
  <div class="pic" role="img" aria-label="Photo of a hand holding a red die" style="background:linear-gradient(135deg,#d9b89a,#9a2a22 55%,#3a1410)"></div>
  <p style="top:212px">Our systems can create randomization data for all types of CTM requirements. Patient randomization, material randomization and random...</p>
  <div class="btn" style="top:311px">Learn More <span>+</span></div>
</div>

<div class="abs sep" style="top:1547px"></div>

<section class="about">
  <div class="abs brand"><i class="mark"></i>MERIDANE WORKS</div>
  <div class="abs vline" style="left:555px;top:1600px;height:308px"></div>
  <h3 class="abs">About Us</h3>
  <p class="abs">Meridane Works, Inc. specializes in providing products and services to the pharmaceutical industry. We are focused on the needs of those individuals involved with Clinical Trial Materials. Our products and services are summarized below:</p>
  <div class="abs links" style="left:626px;top:1770px">MeriServ™<br>MeriBook™<br>MeriPro/LBL™</div>
  <div class="abs links" style="left:782px;top:1770px">Clinical Randomizations<br>Software Validation Services<br>MeriStock™</div>
</section>

<div class="abs sep" style="top:1948px"></div>

<footer class="foot">
  <h5 class="abs" style="left:123px;top:1983px">Navigation</h5>
  <ul class="abs" style="left:123px;top:2022px"><li>Home</li><li>About Us</li><li>Services</li><li>Products</li><li>User Support</li><li>Contact Us</li></ul>
  <h5 class="abs" style="left:288px;top:1983px">Products &amp; Services</h5>
  <ul class="abs" style="left:288px;top:2030px"><li>MeriServ</li><li>MeriBook</li><li>Randomizations</li><li>MeriPro/LBL Validation</li><li>MeriStock</li></ul>
  <h5 class="abs" style="left:500px;top:1983px">Follow us</h5>
  <div class="abs" style="left:500px;top:2032px;display:flex;gap:5px"><i class="dot" style="background:#777"></i><i class="dot" style="background:#777"></i><i class="dot" style="background:#777"></i><i class="dot" style="background:#777"></i><i class="dot" style="background:#777"></i></div>
  <div class="abs vline" style="left:709px;top:1970px;height:200px"></div>
  <div class="abs brand"><i class="mark"></i>MERIDANE WORKS</div>
  <address class="abs" style="top:2048px">412 ALDER LANE SUITE 8, RIVERTON<br>NY 10001-0000 USA</address>
  <address class="abs" style="top:2082px">88 HARBOR ROAD, ELMBROOK<br>NJ 07000 USA</address>
  <address class="abs" style="top:2118px">PHONE: &nbsp;+1-555-010-6200</address>
  <address class="abs" style="top:2138px">FAX: &nbsp;&nbsp;&nbsp;&nbsp;&nbsp;+1-555-010-2620</address>
  <div class="abs copy">© 2014 Meridane Works Inc. All rights reserved.</div>
</footer>
</body>
</html>
```